Belford & Company

We are a boutique commercial real estate firm. For our Business card design - sleek, modern, yet high-end/classy. Please see our website: belfordandcompany.example for details.

We currently need 2 business card names and the ability to add/change the business card information -
Name, Title, Address, Office #, Mobile #, Fax, Email and company website.

Industry/Entity Type

Real Estate

Contact Information for Business Card

Business card design - sleek, modern, yet high-end/classy. Please see our website: belfordandcompany.example for details.

Also, we'd like to have our slogan "Careful Work, Lasting Value." somewhere in there. We'd like to make some part of it raised or a different texture if possible.
Color #'s:
blue 19 36 128
light gray 222 222 221
dark gray 107 120 128

Also, we'd like to have our slogan "Careful Work, Lasting Value." somewhere in there. We'd like to make some part of it raised or a different texture if possible - grey on one side and blue on the other - rounded edges preferred. Maybe either metal/silver/grey raised logo on the back. Thank you!!

Requirements
Must have
• Sleek, modern, clean and classy design

```html
<!DOCTYPE html>
<html lang="en">
<head>
<meta charset="utf-8">
<title>Belford &amp; Company — Business Card</title>
<link href="https://fonts.googleapis.com/css2?family=Roboto:wght@400;500&display=swap" rel="stylesheet">
<style>
  :root{
    --brand-blue:#1e43a0;
    --slate-gray:#8e9ea7;
    --light-gray:#dededd;
    --white:#ffffff;
    --backdrop:#2b2b2c;
  }
  *{box-sizing:border-box;margin:0;padding:0}
  html,body{width:1200px;height:960px;overflow:hidden}
  body{background:var(--backdrop);font-family:"Roboto",Arial,sans-serif;position:relative}
  .card{position:absolute;left:250px;width:700px;height:400px;border-radius:14px;overflow:hidden;box-shadow:0 10px 30px rgba(0,0,0,.45)}
  .card--back{top:50px;background:var(--brand-blue)}
  .card--front{top:500px;background:var(--slate-gray)}
  .card__bg{position:absolute;inset:0;width:100%;height:100%}

  .back__mark{position:absolute;left:0;right:0;top:150px;display:flex;align-items:center;justify-content:center;gap:14px}
  .mark-square{width:22px;height:22px;background:var(--light-gray);flex:none}
  .back__name{font-weight:500;font-size:38px;letter-spacing:.5px;color:var(--light-gray)}
  .slogan{position:absolute;left:0;right:0;top:300px;text-align:center;color:var(--white);font-size:17px;font-weight:400;letter-spacing:.4px}

  .front__brand{position:absolute;right:36px;top:44px;display:flex;align-items:center;gap:10px}
  .front__name{font-weight:500;font-size:26px;color:var(--white);line-height:1}
  .front__brand .mark-square{width:16px;height:16px;background:var(--white)}

  .contact{position:absolute;left:44px;top:150px;color:var(--white)}
  .contact__name{font-weight:500;font-size:27px;letter-spacing:.5px;line-height:1}
  .contact__title{font-size:17px;margin-top:4px;letter-spacing:.3px}
  .contact__address{font-size:16px;line-height:1.3;margin-top:20px;margin-left:28px}
  .contact__list{list-style:none;margin-top:14px}
  .contact__list li{display:flex;align-items:center;gap:12px;font-size:16px;line-height:1.4}
  .contact__list svg{width:16px;height:16px;flex:none}
</style>
</head>
<body>

<section class="card card--back" aria-label="Card back">
  <div class="back__mark">
    <span class="mark-square"></span>
    <span class="back__name">Belford &amp; Company</span>
  </div>
  <p class="slogan">Careful Work, Lasting Value.</p>
</section>

<section class="card card--front" aria-label="Card front">
  <svg class="card__bg" viewBox="0 0 700 400" preserveAspectRatio="none" aria-hidden="true">
    <polygon points="210,0 700,0 700,278" fill="var(--brand-blue)"/>
    <polygon points="210,0 700,278 700,312" fill="var(--white)"/>
  </svg>

  <div class="front__brand">
    <span class="mark-square"></span>
    <span class="front__name">Belford &amp; Company</span>
  </div>

  <div class="contact">
    <p class="contact__name">DANIEL HARTLEY</p>
    <p class="contact__title">CEO/FOUNDER</p>
    <p class="contact__address">4120 Harbor View Road<br>Juneau, Alaska 99801</p>
    <ul class="contact__list">
      <li>
        <svg viewBox="0 0 16 16" aria-label="Office"><path d="M3 1.5l3 3-1.6 1.8c.9 2 2.3 3.4 4.3 4.3L10.5 9l3 3-2 2.3C6.3 13.6 2.4 9.7 1 4.2z" fill="var(--white)"/></svg>
        555 210 4471
      </li>
      <li>
        <svg viewBox="0 0 16 16" aria-label="Mobile"><rect x="4" y="1" width="8" height="14" rx="1.5" fill="none" stroke="var(--white)" stroke-width="1.6"/><circle cx="8" cy="12.5" r=".9" fill="var(--white)"/></svg>
        555 318 6092
      </li>
      <li>
        <svg viewBox="0 0 16 16" aria-label="Fax"><rect x="4" y="1.5" width="8" height="5" fill="var(--white)"/><rect x="1.5" y="6" width="13" height="8" rx="1" fill="var(--white)"/></svg>
        555 742 1183
      </li>
      <li>
        <svg viewBox="0 0 16 16" aria-label="Email"><rect x="1" y="3" width="14" height="10" fill="none" stroke="var(--white)" stroke-width="1.5"/><path d="M1 3l7 5.5L15 3" fill="none" stroke="var(--white)" stroke-width="1.5"/></svg>
        info@belfordandcompany.example
      </li>
      <li>
        <svg viewBox="0 0 16 16" aria-label="Website"><circle cx="8" cy="8" r="7" fill="var(--white)"/><path d="M1 8h14M8 1c-3 3.5-3 10.5 0 14M8 1c3 3.5 3 10.5 0 14" fill="none" stroke="var(--slate-gray)" stroke-width="1"/></svg>
        www.belfordandcompany.example
      </li>
    </ul>
  </div>
</section>

</body>
</html>
```